Consulting firm need a professional powerpoint design

A startup Climate change firm needs a powerpoint template design. The design should reflect aspects of climate change adaptation, resilience and environmental sustainability.

The powerpoint design must convey aspects of nature and climate action for a resilient society.

The last slide of the powerpoint must have a allocation for a slogan such as 'Linking science and decision-making'.

Use the colors in the logo and business card for the powerpoint design.

Target Market(s)

Government and industry

Font styles to use
Sans Serif
Other font styles liked:
• nexa font family

Colors
85cae6
abd037
fece3e

Requirements
Must have
• - Colors used in logo and business card
- Convey science and nature
- Professional
Nice to have
• Many pages
Should not have
• Not complicated

```html
<!DOCTYPE html>
<html lang="en">
<head>
<meta charset="utf-8">
<title>Slide – Heading will come here</title>
<link href="https://fonts.googleapis.com/css2?family=Arimo:wght@400;700&display=swap" rel="stylesheet">
<style>
  :root{
    --navy:#2b3556;
    --ink:#1f2a44;
    --text:#222222;
    --label:#3b3b3b;
    --orange:#f28a22;
    --gold:#e2a82a;
    --yellow:#fece3e;
    --blue:#3ea3d3;
    --sky:#85cae6;
    --green:#44a73e;
    --lime:#abd037;
    --leaf-dark:#2f5a1f;
    --leaf-light:#7fb24a;
    --bg:#ffffff;
  }
  *{margin:0;padding:0;box-sizing:border-box}
  html,body{width:1200px;height:675px;overflow:hidden;background:var(--bg)}
  body{font-family:"Arimo",Arial,sans-serif;color:var(--text)}
  .slide{position:relative;width:1200px;height:675px;overflow:hidden;background:var(--bg)}

  .slide-title{position:absolute;left:32px;top:20px;font-size:36px;font-weight:400;color:var(--navy);letter-spacing:.2px}
  .title-rule{position:absolute;left:0;top:83px;width:561px;height:4px;background:linear-gradient(90deg,var(--gold),var(--orange))}

  .feature-icon{position:absolute;left:67px;width:66px;height:66px}
  .feature-icon svg{width:66px;height:66px;display:block}
  .connector{position:absolute;left:97px;width:4px;height:46px;
    background:radial-gradient(circle,var(--navy) 1.6px,transparent 2px) center top/4px 9.5px repeat-y}

  .feature{position:absolute;left:168px;width:430px}
  .feature-label{font-size:20px;color:var(--label);line-height:24px;margin-bottom:8px}
  .feature-question{font-size:18.5px;font-weight:700;color:var(--ink);line-height:22px;margin-bottom:1px}
  .feature-body{font-size:16px;line-height:21.5px;color:var(--text)}

  .photo-frame{position:absolute;left:640px;top:-40px;width:524px;height:624px;border-radius:0 0 56px 56px;
    background:linear-gradient(90deg,var(--gold),var(--orange));padding:14px}
  .photo{width:100%;height:100%;border-radius:0 0 44px 44px;
    background:radial-gradient(ellipse at 50% 55%,var(--leaf-light) 0%,#4f8a33 40%,var(--leaf-dark) 100%)}

  .footer-bands{position:absolute;left:0;top:630px;width:1200px;height:45px}
  .brand{position:absolute;right:24px;top:640px;font-size:22px;font-weight:700;color:#ffffff;letter-spacing:2px;display:flex;align-items:center;gap:10px}
  .brand-dot{width:14px;height:14px;border-radius:50%;background:#ffffff}
</style>
</head>
<body>
<main class="slide">
  <h1 class="slide-title">Heading will come here</h1>
  <div class="title-rule"></div>

  <!-- Feature 1 -->
  <div class="feature-icon" style="top:153px">
    <svg viewBox="0 0 66 66" fill="none" stroke="#2b3556" stroke-width="1.4">
      <circle cx="33" cy="33" r="31.5"/>
      <rect x="18" y="18" width="10" height="10"/><rect x="21" y="21" width="4" height="4" fill="#2b3556"/>
      <rect x="38" y="18" width="10" height="10"/><rect x="41" y="21" width="4" height="4" fill="#2b3556"/>
      <rect x="18" y="38" width="10" height="10"/><rect x="21" y="41" width="4" height="4" fill="#2b3556"/>
      <path d="M32 18v6M32 28h6M38 34h10M34 38v10M40 40h4v8M46 40v4"/>
    </svg>
  </div>
  <div class="connector" style="top:236px"></div>
  <section class="feature" style="top:160px">
    <p class="feature-label">ICON 1</p>
    <h2 class="feature-question">How are you solving the problem?</h2>
    <p class="feature-body">Sales &amp; Marketing are expensive.<br>we make these more effective by<br>focusing on thttttte right blend of<br>techniques on the right segment</p>
  </section>

  <!-- Feature 2 -->
  <div class="feature-icon" style="top:311px">
    <svg viewBox="0 0 66 66" fill="none" stroke="#2b3556" stroke-width="1.4" stroke-linecap="round">
      <circle cx="33" cy="33" r="31.5"/>
      <circle cx="33" cy="17" r="3"/>
      <path d="M33 20v28M27 26h12"/>
      <path d="M16 36c2 8 9 12 17 12s15-4 17-12"/>
      <path d="M13 38l3-3 3 3M47 38l3-3 3 3"/>
    </svg>
  </div>
  <div class="connector" style="top:396px"></div>
  <section class="feature" style="top:320px">
    <p class="feature-label">ICON 2</p>
    <h2 class="feature-question">What’s your unique approach ?</h2>
    <p class="feature-body">Every project that we do is highly<br>customized &amp; targeted and involves<br>deep research thus involving human<br>intelligence at every step.</p>
  </section>

  <!-- Feature 3 -->
  <div class="feature-icon" style="top:471px">
    <svg viewBox="0 0 66 66" fill="none" stroke="#2b3556" stroke-width="1.4" stroke-linecap="round">
      <circle cx="33" cy="33" r="31.5"/>
      <ellipse cx="35" cy="17" rx="5" ry="2.5"/><ellipse cx="43" cy="20" rx="5" ry="2.5"/>
      <ellipse cx="37" cy="25" rx="5" ry="2.5"/><ellipse cx="42" cy="31" rx="5" ry="2.5"/>
      <rect x="12" y="34" width="6" height="15"/>
      <path d="M18 36h9c3 0 4 3 1 4h-6M18 47h16l14-9c2-2 0-4-2-3l-10 5"/>
    </svg>
  </div>
  <section class="feature" style="top:480px">
    <p class="feature-label">ICON 3</p>
    <h2 class="feature-question">What else do you offer nobody else does ?</h2>
    <p class="feature-body">We offer highly customized solutions and<br>fully integrated broad portfolio</p>
  </section>

  <!-- Visual -->
  <div class="photo-frame">
    <div class="photo" role="img" aria-label="Photo of cupped hands holding a young seedling in soil, ringed by sustainability icons on a soft green background"></div>
  </div>

  <!-- Footer -->
  <svg class="footer-bands" viewBox="0 0 1200 45" preserveAspectRatio="none">
    <defs>
      <linearGradient id="band-warm" x1="0" x2="1"><stop offset="0" stop-color="#f28a22"/><stop offset="1" stop-color="#fece3e"/></linearGradient>
      <linearGradient id="band-cool" x1="0" x2="1"><stop offset="0" stop-color="#1f7fa8"/><stop offset="1" stop-color="#85cae6"/></linearGradient>
      <linearGradient id="band-fresh" x1="0" x2="1"><stop offset="0" stop-color="#44a73e"/><stop offset="1" stop-color="#abd037"/></linearGradient>
    </defs>
    <polygon points="0,10 300,10 293,18 0,18" fill="url(#band-warm)"/>
    <polygon points="300,10 615,10 608,18 293,18" fill="url(#band-cool)"/>
    <polygon points="622,10 922,10 915,18 615,18" fill="url(#band-fresh)"/>
    <polygon points="0,18 915,18 940,2 1200,2 1200,45 0,45" fill="#363f5c"/>
  </svg>
  <div class="brand"><span class="brand-dot"></span>VERDALINE</div>
</main>
</body>
</html>
```